Local Horticulturalist needs Business card design

Meridale Gardening would like to update our existing business card and utilize our new logo (design attached)....we specialize in getting the best out of our customers yard with professional maintenance programs, expert pruning and hedging and garden restorations.
Utilizing colors from attached logo I would like a design that implies professionalism and if possible our businesses love of restoration through plants.
I also sometimes write down for my customers a start date and price on the back of my current card
Target Market(s)
Home owners
Contractors
Industry/Entity Type
Gardener
Contact Information for Business Card
Trevor Kalbrook | Horticulturalist
ph: 0452739186
meridalegard@fernpost.com
www.meridalegardening.com.au
Requirements
Must have
- crucial information easy to read
- incorporate current logo
- Horticulturalist listed preferably near name
Nice to have
- currently I write a job start date and price on the back of my current card so something that integrates this would be beneficial
Should not have
- be pretty or flowerey
- be too white or basic

```html
<!DOCTYPE html>
<html lang="en">
<head>
<meta charset="utf-8">
<title>Meridale Gardening – Business Card</title>
<link href="https://fonts.googleapis.com/css2?family=Cabin:wght@600;700&family=Open+Sans:wght@400;600&display=swap" rel="stylesheet">
<style>
  :root {
    --backdrop: #d9d9d9;
    --card-black: #0d0d0d;
    --card-charcoal: #262626;
    --card-white: #ffffff;
    --leaf-green: #6cba2f;
    --leaf-green-light: #8ad33f;
    --taupe: #8a7f72;
    --taupe-dark: #5f574e;
    --ink: #4a4a4a;
  }
  * { margin: 0; padding: 0; box-sizing: border-box; }
  html, body { width: 1200px; height: 852px; overflow: hidden; }
  body {
    background: var(--backdrop);
    position: relative;
    font-family: "Open Sans", Arial, sans-serif;
  }
  .card {
    position: absolute;
    width: 600px;
    height: 343px;
    border-radius: 22px;
    overflow: hidden;
    box-shadow: 0 6px 18px rgba(0,0,0,0.25);
  }

  /* Front */
  .card--front {
    left: 180px; top: 48px;
    background: linear-gradient(150deg, var(--card-charcoal) 0%, var(--card-black) 55%, #1b1b1b 100%);
  }
  .front-mark {
    position: absolute;
    left: 255px; top: 62px;
    width: 90px; height: 90px;
    border-radius: 50%;
    background: var(--leaf-green);
  }
  .front-name {
    position: absolute;
    left: 0; right: 0; top: 168px;
    text-align: center;
    font-family: "Cabin", Arial, sans-serif;
    font-weight: 700;
    font-size: 40px;
    color: var(--leaf-green);
    letter-spacing: 0.5px;
  }
  .front-tagline {
    position: absolute;
    left: 0; right: 0; top: 220px;
    text-align: center;
    font-family: "Cabin", Arial, sans-serif;
    font-weight: 600;
    font-size: 21px;
    color: var(--taupe);
    letter-spacing: 1px;
  }

  /* Back */
  .card--back {
    left: 420px; top: 460px;
    background: var(--card-white);
  }
  .back-shape { position: absolute; inset: 0; }
  .back-mark {
    position: absolute;
    left: 50px; top: 105px;
    width: 132px; height: 132px;
    border-radius: 50%;
    background: var(--leaf-green);
  }
  .back-info {
    position: absolute;
    left: 292px; top: 36px;
    width: 290px;
  }
  .back-name {
    font-family: "Cabin", Arial, sans-serif;
    font-weight: 700;
    font-size: 27px;
    line-height: 1;
    color: var(--leaf-green);
  }
  .back-tagline {
    margin-top: 5px;
    font-family: "Cabin", Arial, sans-serif;
    font-weight: 600;
    font-size: 13.5px;
    color: var(--taupe-dark);
    letter-spacing: 0.6px;
  }
  .person {
    margin-top: 62px;
  }
  .person-name {
    font-weight: 600;
    font-size: 17px;
    color: var(--leaf-green);
  }
  .person-title {
    font-size: 11.5px;
    color: var(--ink);
    margin-top: 1px;
  }
  .contact-list {
    list-style: none;
    margin-top: 20px;
  }
  .contact-item {
    display: flex;
    align-items: center;
    gap: 10px;
    font-size: 13px;
    color: var(--ink);
    line-height: 21px;
  }
  .contact-icon { width: 13px; height: 13px; flex: none; }
</style>
</head>
<body>

<section class="card card--front" aria-label="Business card front">
  <div class="front-mark"></div>
  <h1 class="front-name">Meridale Gardening</h1>
  <p class="front-tagline">Garden Restorations &amp; Maintenance</p>
</section>

<section class="card card--back" aria-label="Business card back">
  <svg class="back-shape" viewBox="0 0 600 343" width="600" height="343" aria-hidden="true">
    <defs>
      <linearGradient id="panel-black" x1="0" y1="0" x2="1" y2="1">
        <stop offset="0" stop-color="#2a2a2a"/>
        <stop offset="0.6" stop-color="#0d0d0d"/>
        <stop offset="1" stop-color="#1a1a1a"/>
      </linearGradient>
    </defs>
    <path d="M0 0 H190 C225 90 262 220 238 343 H0 Z" fill="#8a7f72"/>
    <path d="M0 0 H180 C212 90 244 220 222 343 H0 Z" fill="#6cba2f"/>
    <path d="M0 0 H172 C202 90 232 220 210 343 H0 Z" fill="url(#panel-black)"/>
  </svg>
  <div class="back-mark"></div>

  <div class="back-info">
    <h2 class="back-name">Meridale Gardening</h2>
    <p class="back-tagline">Garden Restorations &amp; Maintenance</p>

    <div class="person">
      <p class="person-name">Trevor Kalbrook</p>
      <p class="person-title">Horticulturalist</p>
    </div>

    <ul class="contact-list">
      <li class="contact-item">
        <svg class="contact-icon" viewBox="0 0 16 16" aria-hidden="true"><path d="M2 5c0-2 3-3 6-3s6 1 6 3v1h-3V5H5v1H2z M4 8h8l2 6H2z" fill="#6cba2f"/></svg>
        0452739186
      </li>
      <li class="contact-item">
        <svg class="contact-icon" viewBox="0 0 16 16" aria-hidden="true"><rect x="1" y="3" width="14" height="10" fill="#6cba2f"/><path d="M1 3l7 6 7-6" fill="none" stroke="#fff" stroke-width="1.4"/></svg>
        meridalegard@fernpost.com
      </li>
      <li class="contact-item">
        <svg class="contact-icon" viewBox="0 0 16 16" aria-hidden="true"><circle cx="8" cy="8" r="7" fill="#6cba2f"/><path d="M1 8h14M8 1c-3 4-3 10 0 14M8 1c3 4 3 10 0 14" fill="none" stroke="#fff" stroke-width="1"/></svg>
        www.meridalegardening.com.au
      </li>
    </ul>
  </div>
</section>

</body>
</html>
```